Powerpoint deck to compliment logo

We have and like our logo. We need a standard PowerPoint deck to use in our many and varied presentations. We are happy with how we format them, but we need a template that compliments our logo. We are about health, wellness and safety in schools. We don't want a 'theme' which is too angular, but we do want color blocks, occasionally, within the templates. The deck should compliment our existing logo.

Target Market(s)

Employees

Industry/Entity Type

Healthcare, education and safety

Font styles to use
Serif
Other font styles liked:
• Century Schoolbook

Colors

Designer to choose colors to be used in the design.

Requirements
Must have
• colors which compliment our logo.
Nice to have
• Fluid objects
Should not have
• Angles

```html
<!DOCTYPE html>
<html lang="en">
<head>
<meta charset="utf-8">
<title>Harbor Valley Schools Wellness Programs – Presentation Template</title>
<link href="https://fonts.googleapis.com/css2?family=Old+Standard+TT:wght@400;700&family=Roboto:wght@400;500;700&display=swap" rel="stylesheet">
<style>
:root{
  --navy:#2e3388;
  --navy-deep:#262a78;
  --green:#6fa83a;
  --green-light:#9ccc65;
  --blue:#5b8fc9;
  --blue-light:#8db4e0;
  --stage:#7b7b7b;
  --ink:#222;
  --muted:#555;
  --row:#f0f0f2;
  --white:#fff;
  --serif:"Old Standard TT", "Century Schoolbook", Georgia, serif;
  --sans:"Roboto", Arial, sans-serif;
}
*{margin:0;padding:0;box-sizing:border-box}
html,body{width:989px;height:1200px;overflow:hidden;background:var(--stage)}
.canvas{position:relative;width:989px;height:1200px;background:var(--stage);font-family:var(--sans);color:var(--ink)}
.slide{position:absolute;width:430px;height:242px;background:var(--white);overflow:hidden}
.col-left{left:48px}.col-right{left:512px}
.row-1{top:58px}.row-2{top:338px}.row-3{top:619px}.row-4{top:900px}
.abs{position:absolute}
svg.fill{position:absolute;left:0;top:0}

/* header band */
.slide-heading{position:absolute;left:26px;top:18px;font-family:var(--serif);font-size:12.5px;color:var(--white);letter-spacing:.4px;white-space:nowrap}
.slide-heading b{font-weight:700}
.brand-tag{position:absolute;right:8px;top:10px;width:46px;text-align:center;font-family:var(--serif);font-size:5.4px;line-height:1.15;color:var(--navy)}
.brand-tag .dot{display:block;width:18px;height:18px;border-radius:50%;background:var(--green);margin:0 auto 3px}

/* title slide */
.title-slide{background:var(--navy)}
.title-brand{position:absolute;left:26px;top:22px;font-family:var(--serif);font-size:7px;line-height:1.2;color:var(--white)}
.title-brand .dot{display:block;width:30px;height:30px;border-radius:50%;background:var(--white);margin-bottom:5px}
.title-main{position:absolute;left:26px;top:100px;font-family:var(--serif);font-size:14.5px;line-height:1.3;color:var(--white);letter-spacing:.3px}
.title-main b{font-weight:700}
.title-rule{position:absolute;left:26px;top:141px;width:30px;height:1.5px;background:var(--green)}
.title-sub{position:absolute;left:26px;top:152px;width:180px;font-size:7.4px;line-height:1.65;color:var(--white)}

/* text blocks */
.lead{font-size:8.3px;font-weight:700;line-height:1.35;color:#111}
.body{font-size:5.1px;line-height:1.8;color:var(--muted)}
.ticks{list-style:none}
.ticks li{position:relative;padding-left:10px;font-size:5.1px;line-height:1.8;color:var(--muted);margin-top:3px}
.ticks li::before{content:"";position:absolute;left:0;top:2.2px;width:5px;height:5px;border-radius:50%;background:var(--green)}
.ticks li.navy::before{background:var(--navy)}
.feature h4{font-size:6px;font-weight:700;color:#111;margin-bottom:5px}
.feature p{font-size:4.8px;line-height:1.75;color:var(--muted)}
.feature.right-align{text-align:right}

/* stats */
.stat{position:absolute;border-radius:50%;color:var(--white);text-align:center;display:flex;flex-direction:column;align-items:center;justify-content:center}
.stat .num{font-family:var(--serif);font-size:13px;letter-spacing:.5px;margin:4px 0 3px}
.stat .cap{font-size:6px;line-height:1.4;width:78%}
.stat-navy{background:linear-gradient(180deg,#3b48a5,var(--navy-deep))}
.stat-green{background:linear-gradient(180deg,var(--green-light),var(--green))}
.stat-blue{background:linear-gradient(180deg,var(--blue-light),var(--blue))}

/* section break */
.section-slide{background:linear-gradient(180deg,#a1d06a,#6ea43c)}
.section-title{position:absolute;left:0;right:0;top:144px;text-align:center;font-family:var(--serif);font-size:17px;color:var(--white);letter-spacing:.8px}
.section-brand{position:absolute;left:0;right:0;top:100px;text-align:center;font-family:var(--serif);font-size:9px;color:var(--white)}

/* table */
.grid-head{position:absolute;top:79px;width:94px;height:14px;color:var(--white);font-size:5.6px;font-weight:700;display:flex;align-items:center;justify-content:center}
.grid-head::after{content:"";position:absolute;left:50%;bottom:-3px;margin-left:-3px;border-left:3px solid transparent;border-right:3px solid transparent;border-top:3px solid currentColor}
.grid-head.navy{background:var(--navy);color:var(--white)}
.grid-head.navy::after{border-top-color:var(--navy)}
.grid-head.green{background:var(--green)}
.grid-head.green::after{border-top-color:var(--green)}
.icon-rail{position:absolute;left:51px;top:92px;width:26px;height:115px;background:var(--blue)}
.icon-rail span{position:absolute;left:8px;width:10px;height:10px;border-radius:50%;border:1.5px solid var(--white)}
.grid-row{position:absolute;left:77px;width:303px;height:20px;display:flex;font-size:4.8px;color:#333}
.grid-row.alt{background:var(--row)}
.grid-row div{flex:1;display:flex;align-items:center;justify-content:center}

/* vision */
.badge{position:absolute;width:34px;height:34px;border-radius:50%}
.badge.navy{background:linear-gradient(180deg,#3b48a5,var(--navy-deep))}
.badge.green{background:linear-gradient(180deg,var(--green-light),var(--green))}
.badge::after{content:"";position:absolute;left:10px;top:10px;width:14px;height:14px;border-radius:50%;border:1.5px solid var(--white)}
.vm{position:absolute;left:67px;width:125px}
.vm h4{font-size:6px;font-weight:700;color:#111;margin-bottom:5px}
.vm p{font-size:4.9px;line-height:1.75;color:var(--muted)}
.axis{font-size:5px;font-weight:700;fill:#333;font-family:var(--sans)}
.val{font-size:4.8px;font-weight:700;fill:#222;font-family:var(--sans)}
</style>
</head>
<body>
<div class="canvas">

  <!-- Title slide -->
  <section class="slide title-slide col-left row-1">
    <svg class="fill" width="430" height="242" viewBox="0 0 430 242">
      <defs>
        <linearGradient id="sky" x1="0" y1="0" x2="0" y2="1">
          <stop offset="0" stop-color="#9cbcd8"/><stop offset=".45" stop-color="#c9b49a"/><stop offset="1" stop-color="#3f5a34"/>
        </linearGradient>
      </defs>
      <rect x="170" y="0" width="260" height="242" fill="url(#sky)" role="img" aria-label="Photo of a woman with closed eyes enjoying fresh air in front of a forest"/>
      <path d="M175 242 C 255 170 262 70 190 0" fill="none" stroke="var(--blue)" stroke-width="9"/>
      <path d="M175 242 C 250 170 254 70 180 0" fill="none" stroke="var(--green)" stroke-width="5"/>
      <path d="M0 0 H178 C 248 70 242 170 168 242 H0 Z" fill="var(--navy)"/>
    </svg>
    <div class="title-brand"><span class="dot"></span>Harbor Valley Schools<br>Wellness Programs</div>
    <h1 class="title-main">HARBOR VALLEY SCHOOLS<br>WELLNESS PROGRAMS</h1>
    <div class="title-rule"></div>
    <p class="title-sub">An active employee or the spouse, registered domestic partner or child of an active employee</p>
  </section>

  <!-- Vision plan slide -->
  <section class="slide col-right row-1">
    <svg class="fill" width="430" height="242" viewBox="0 0 430 242">
      <path d="M0 0 H370 C358 28 345 41 318 41 H40 C16 41 0 52 0 64 Z" fill="var(--navy)"/>
      <circle cx="109" cy="143" r="80" fill="var(--green)"/>
      <circle cx="109" cy="143" r="74" fill="var(--blue)"/>
      <circle cx="109" cy="143" r="70" fill="#d9a98a" role="img" aria-label="Photo of two smiling people showing bandages after a vaccination"/>
    </svg>
    <h2 class="slide-heading"><b>SLIDE HEADING</b> GOES HERE</h2>
    <div class="brand-tag"><span class="dot"></span>Harbor Valley<br>Schools</div>
    <div class="abs" style="left:214px;top:60px;width:190px">
      <p class="lead">HVWP's self-funded vision plans are administered by ClearSight.</p>
      <p class="body" style="margin-top:7px">Each employer and/or bargaining unit has determined the plan(s) from which you may select your coverage effective October 1 through September 30. You may select a plan from that menu if you are ...</p>
      <ul class="ticks" style="margin-top:2px">
        <li>An active employee or the spouse, registered domestic partner or child of an active employee</li>
        <li>A retiree not yet eligible for Medicare</li>
        <li>The spouse or registered domestic partner of a retiree AND you are not yet eligible for Medicare (regardless of the retiree's Medicare status)</li>
      </ul>
      <p class="body" style="margin-top:4px">Log in to your secure ClearSight account to view your benefit details, the status of your claims, find a network provider and download forms. You will also find great wellness information as well as information on discounts available for non-covered Laser services, etc.</p>
    </div>
  </section>

  <!-- Wheel slide -->
  <section class="slide col-left row-2">
    <svg class="fill" width="430" height="242" viewBox="0 0 430 242">
      <path d="M0 0 H370 C358 28 345 41 318 41 H40 C16 41 0 52 0 64 Z" fill="var(--navy)"/>
      <g transform="rotate(-90 215 145)">
        <circle cx="215" cy="145" r="53" fill="none" stroke="var(--green)" stroke-width="34" stroke-dasharray="52 59"/>
        <circle cx="215" cy="145" r="53" fill="none" stroke="var(--blue)" stroke-width="34" stroke-dasharray="52 59" stroke-dashoffset="-55.5"/>
      </g>
      <circle cx="215" cy="145" r="36" fill="var(--white)"/>
    </svg>
    <h2 class="slide-heading"><b>SLIDE HEADING</b> GOES HERE</h2>
    <div class="brand-tag"><span class="dot"></span>Harbor Valley<br>Schools</div>
    <div class="abs" style="left:192px;top:135px;width:46px;text-align:center;font-family:var(--serif);font-size:6px;color:var(--navy);line-height:1.2">Harbor Valley<br>Schools</div>
    <div class="feature right-align abs" style="left:26px;top:68px;width:105px"><h4>Lorem ipsum dolor sit amet</h4><p>Sed ut perspiciatis unde omnis iste natus error sit voluptatem accusantium laudantium, totam eaque ipsa rem aperiam</p></div>
    <div class="feature right-align abs" style="left:26px;top:128px;width:105px"><h4>Lorem ipsum dolor sit amet</h4><p>Sed ut perspiciatis unde omnis iste natus error sit voluptatem accusantium laudantium, totam eaque ipsa rem aperiam</p></div>
    <div class="feature right-align abs" style="left:26px;top:187px;width:105px"><h4>Lorem ipsum dolor sit amet</h4><p>Sed ut perspiciatis unde omnis iste natus error sit voluptatem accusantium laudantium, totam eaque ipsa rem aperiam</p></div>
    <div class="feature abs" style="left:297px;top:68px;width:110px"><h4>Lorem ipsum dolor sit amet</h4><p>Sed ut perspiciatis unde omnis iste natus error sit voluptatem accusantium laudantium, totam eaque ipsa rem aperiam</p></div>
    <div class="feature abs" style="left:297px;top:128px;width:110px"><h4>Lorem ipsum dolor sit amet</h4><p>Sed ut perspiciatis unde omnis iste natus error sit voluptatem accusantium laudantium, totam eaque ipsa rem aperiam</p></div>
    <div class="feature abs" style="left:297px;top:187px;width:110px"><h4>Lorem ipsum dolor sit amet</h4><p>Sed ut perspiciatis unde omnis iste natus error sit voluptatem accusantium laudantium, totam eaque ipsa rem aperiam</p></div>
  </section>

  <!-- Chart slide -->
  <section class="slide col-right row-2">
    <svg class="fill" width="430" height="242" viewBox="0 0 430 242">
      <path d="M0 0 H370 C358 28 345 41 318 41 H40 C16 41 0 52 0 64 Z" fill="var(--navy)"/>
      <g stroke="#e3e3e3" stroke-width=".6">
        <line x1="36" y1="64" x2="267" y2="64"/><line x1="36" y1="88" x2="267" y2="88"/><line x1="36" y1="112" x2="267" y2="112"/>
        <line x1="36" y1="136" x2="267" y2="136"/><line x1="36" y1="160" x2="267" y2="160"/><line x1="36" y1="184" x2="267" y2="184"/>
        <line x1="36" y1="208" x2="267" y2="208"/>
        <line x1="36" y1="64" x2="36" y2="208"/><line x1="69" y1="64" x2="69" y2="208"/><line x1="102" y1="64" x2="102" y2="208"/><line x1="135" y1="64" x2="135" y2="208"/><line x1="168" y1="64" x2="168" y2="208"/><line x1="201" y1="64" x2="201" y2="208"/><line x1="234" y1="64" x2="234" y2="208"/><line x1="267" y1="64" x2="267" y2="208"/>
      </g>
      <g class="axis" text-anchor="end">
        <text x="32" y="66">120</text><text x="32" y="90">100</text><text x="32" y="114">80</text><text x="32" y="138">60</text><text x="32" y="162">40</text><text x="32" y="186">20</text><text x="32" y="210">0</text>
      </g>
      <g class="axis" text-anchor="middle">
        <text x="53" y="217">Sun</text><text x="86" y="217">Mon</text><text x="119" y="217">Tue</text><text x="152" y="217">Wed</text><text x="185" y="217">Thu</text><text x="218" y="217">Fri</text><text x="250" y="217">Sat</text>
      </g>
      <g fill="var(--blue)">
        <rect x="45" y="88" width="6" height="120"/><rect x="78" y="100" width="6" height="108"/><rect x="111" y="148" width="6" height="60"/>
        <rect x="144" y="88" width="6" height="120"/><rect x="177" y="88" width="6" height="120"/><rect x="210" y="136" width="6" height="72"/><rect x="242" y="148" width="6" height="60"/>
      </g>
      <g fill="var(--green-light)">
        <rect x="55" y="100" width="6" height="108"/><rect x="88" y="112" width="6" height="96"/><rect x="121" y="88" width="6" height="120"/>
        <rect x="154" y="136" width="6" height="72"/><rect x="187" y="100" width="6" height="108"/><rect x="220" y="118" width="6" height="90"/><rect x="252" y="88" width="6" height="120"/>
      </g>
      <g class="val" text-anchor="middle">
        <text x="48" y="85">100</text><text x="58" y="97">90</text><text x="81" y="97">90</text><text x="91" y="109">80</text>
        <text x="114" y="145">50</text><text x="124" y="85">100</text><text x="147" y="85">100</text><text x="157" y="133">60</text>
        <text x="180" y="85">100</text><text x="190" y="97">90</text><text x="213" y="133">60</text><text x="223" y="115">75</text>
        <text x="245" y="145">50</text><text x="255" y="85">100</text>
      </g>
    </svg>
    <h2 class="slide-heading"><b>SLIDE HEADING</b> GOES HERE</h2>
    <div class="brand-tag"><span class="dot"></span>Harbor Valley<br>Schools</div>
    <ul class="ticks abs" style="left:287px;top:60px;width:125px">
      <li>Lorem ipsum dolor sit consectetur adipiscing elit, sed do eiusmod tempor incididunt ut labore et dolore magna aliqua.</li>
      <li>Lorem ipsum dolor sit consectetur adipiscing elit, sed do eiusmod</li>
      <li>Lorem ipsum dolor sit consectetur adipiscing elit, sed do eiusmod tempor incididunt ut labore et dolore magna aliqua.</li>
      <li>Lorem ipsum dolor sit consectetur adipiscing elit, sed do eiusmod</li>
      <li>Lorem ipsum dolor sit consectetur adipiscing elit, sed do eiusmod tempor incididunt ut labore et dolore magna aliqua.</li>
      <li class="navy">Lorem ipsum dolor sit consectetur adipiscing elit, sed do eiusmod</li>
    </ul>
  </section>

  <!-- Stats slide -->
  <section class="slide col-left row-3">
    <svg class="fill" width="430" height="242" viewBox="0 0 430 242">
      <path d="M0 0 H370 C358 28 345 41 318 41 H40 C16 41 0 52 0 64 Z" fill="var(--navy)"/>
    </svg>
    <h2 class="slide-heading"><b>SLIDE HEADING</b> GOES HERE</h2>
    <div class="brand-tag"><span class="dot"></span>Harbor Valley<br>Schools</div>
    <div class="stat stat-navy" style="left:28px;top:91px;width:109px;height:109px">
      <svg width="24" height="24" viewBox="0 0 24 24" fill="none" stroke="#fff" stroke-width="1.4"><circle cx="11" cy="13" r="9"/><path d="M11 4v9h9"/><path d="M14 2a9 9 0 0 1 8 8h-8z"/></svg>
      <div class="num">19.29%</div><div class="cap">Lorem ipsum dolor sit amet, consectetur magna elit</div>
    </div>
    <div class="stat stat-green" style="left:150px;top:71px;width:130px;height:130px">
      <svg width="38" height="30" viewBox="0 0 38 30" fill="none" stroke="#fff" stroke-width="1.3"><circle cx="20" cy="7" r="6"/><path d="M20 4v6M18 5.5h3.5a1 1 0 0 1 0 2h-3a1 1 0 0 0 0 2H22"/><path d="M2 24l8-7h8a2 2 0 0 1 0 4h-5M17 21l10-5a2 2 0 0 1 2 3l-10 7H8"/></svg>
      <div class="num" style="font-size:15px">$39 MILLION</div><div class="cap">Lorem ipsum sit amet, consectetur adipiscing elit, ut dolore sed do veniam magna aliqua.</div>
    </div>
    <div class="stat stat-blue" style="left:295px;top:91px;width:109px;height:109px">
      <svg width="22" height="26" viewBox="0 0 22 26" fill="none" stroke="#fff" stroke-width="1.4"><path d="M11 1l9 4v7c0 6-4 10-9 12C6 22 2 18 2 12V5z"/><path d="M6.5 13l3 3 6-6"/></svg>
      <div class="num">19/59</div><div class="cap">Lorem ipsum dolor sit amet, consectetur magna elit</div>
    </div>
  </section>

  <!-- Section break -->
  <section class="slide section-slide col-right row-3">
    <div class="section-brand">Harbor Valley Schools</div>
    <h2 class="section-title">SECTION BREAK</h2>
  </section>

  <!-- Table slide -->
  <section class="slide col-left row-4">
    <svg class="fill" width="430" height="242" viewBox="0 0 430 242">
      <path d="M0 0 H370 C358 28 345 41 318 41 H40 C16 41 0 52 0 64 Z" fill="var(--navy)"/>
    </svg>
    <h2 class="slide-heading"><b>SLIDE HEADING</b> GOES HERE</h2>
    <div class="brand-tag"><span class="dot"></span>Harbor Valley<br>Schools</div>
    <div class="grid-head navy" style="left:97px">Text Here</div>
    <div class="grid-head green" style="left:191px">Text Here</div>
    <div class="grid-head navy" style="left:286px">Text Here</div>
    <div class="icon-rail"><span style="top:7px"></span><span style="top:29px"></span><span style="top:50px"></span><span style="top:71px"></span><span style="top:91px"></span></div>
    <div class="grid-row alt" style="top:99px"><div>Add Contents Title</div><div>Add Contents Title</div><div>Add Contents Title</div></div>
    <div class="grid-row" style="top:119px"><div>Add Contents Title</div><div>Add Contents Title</div><div>Add Contents Title</div></div>
    <div class="grid-row alt" style="top:139px"><div>Add Contents Title</div><div>Add Contents Title</div><div>Add Contents Title</div></div>
    <div class="grid-row" style="top:159px"><div>Add Contents Title</div><div>Add Contents Title</div><div>Add Contents Title</div></div>
    <div class="grid-row alt" style="top:178px"><div>Add Contents Title</div><div>Add Contents Title</div><div>Add Contents Title</div></div>
  </section>

  <!-- Vision & mission slide -->
  <section class="slide col-right row-4">
    <svg class="fill" width="430" height="242" viewBox="0 0 430 242">
      <defs>
        <linearGradient id="screen" x1="0" y1="0" x2="1" y2="1">
          <stop offset="0" stop-color="#6f9fcf"/><stop offset="1" stop-color="#132a4f"/>
        </linearGradient>
      </defs>
      <path d="M0 0 H370 C358 28 345 41 318 41 H40 C16 41 0 52 0 64 Z" fill="var(--navy)"/>
      <path d="M222 160 L318 70 Q325 66 332 70 L400 118 Q405 124 400 130 L300 205 Q293 209 287 205 L224 170 Q218 165 222 160 Z" fill="url(#screen)" role="img" aria-label="Tablet showing a photo of scientists working in a modern lab"/>
    </svg>
    <h2 class="slide-heading"><b>SLIDE HEADING</b> GOES HERE</h2>
    <div class="brand-tag"><span class="dot"></span>Harbor Valley<br>Schools</div>
    <div class="badge navy" style="left:25px;top:86px"></div>
    <div class="vm" style="top:90px"><h4>Vision</h4><p>At vero eos et accusamus et iusto dignissimos ducimus qui blanditiis praesentium voluptatum deleniti atque corrupti</p></div>
    <div class="badge green" style="left:25px;top:142px"></div>
    <div class="vm" style="top:146px"><h4>Mission</h4><p>Sed ut perspiciatis unde omnis iste natus error sit voluptatem accusantium doloremque laudantium, totam rem aperiam, eaque ipsa quae ab illo inventore veritatis et quasi</p></div>
  </section>

</div>
</body>
</html>
```